Norvane Builders Business Card

Modern and Professional Business Card for a Med size construction/development company.

See the samples below for the design I like … but I need ideas for incorporating the red company logo while still keeping the clean look of the card samples that are attached.

Logo and tag line on the back … info on the front.

Tagline: Quality Starts from the Ground Up

Target Market(s)

Med-Large General Contractors

Contact Information for Business Card

Norvane Builders Limited
42 Brenton Street
Elk Harbour, NL
B3K 7T2

t: 709-555-0147
f: 709-555-0192
w: www.norvanebuilders-example.com

Font styles to use
Sans Serif

Colors
fbee3e

Requirements
Must have
• I like the black and yellow designs of the attached samples …. but I'm not sure how to incorporate the red Norvane Builders logo into that design??
Nice to have
• Construction safety strips

```html
<!DOCTYPE html>
<html lang="en">
<head>
<meta charset="utf-8">
<title>Norvane Builders Business Card</title>
<link rel="stylesheet" href="https://fonts.googleapis.com/css2?family=Lato:wght@300;400;700;900&display=swap">
<style>
  :root {
    --backdrop: #3b3b3d;
    --card-dark: #2b2b2d;
    --brand-red: #e31e24;
    --accent-yellow: #fbee3e;
    --ink-light: #ffffff;
    --ink-dark: #1e1e20;
  }
  * { margin: 0; padding: 0; box-sizing: border-box; }
  html, body {
    width: 1200px;
    height: 960px;
    overflow: hidden;
    background: var(--backdrop);
    font-family: "Lato", Arial, sans-serif;
  }
  .canvas {
    position: relative;
    width: 1200px;
    height: 960px;
    display: flex;
    flex-direction: column;
    align-items: center;
    justify-content: center;
    gap: 50px;
  }
  .card {
    display: block;
    width: 700px;
    height: 400px;
    box-shadow: 0 14px 30px rgba(0,0,0,0.45);
  }
  .card-bg { fill: var(--card-dark); }
  .card-red { fill: var(--brand-red); }
  .brand-name {
    font-family: "Lato", Arial, sans-serif;
    font-weight: 900;
    fill: var(--ink-dark);
    letter-spacing: 1px;
  }
  .tagline {
    font-family: "Lato", Arial, sans-serif;
    font-weight: 400;
    font-size: 15px;
    fill: var(--accent-yellow);
    letter-spacing: 1.5px;
  }
  .site-url {
    font-family: "Lato", Arial, sans-serif;
    font-weight: 400;
    font-size: 19px;
    fill: var(--ink-light);
    letter-spacing: 1.5px;
  }
  .person-first { font-weight: 900; fill: var(--ink-light); }
  .person-last { font-weight: 300; fill: var(--ink-light); }
  .person-name { font-family: "Lato", Arial, sans-serif; font-size: 27px; }
  .person-role {
    font-family: "Lato", Arial, sans-serif;
    font-weight: 400;
    font-size: 16px;
    fill: var(--brand-red);
  }
  .contact-line {
    font-family: "Lato", Arial, sans-serif;
    font-weight: 400;
    font-size: 17px;
    fill: var(--ink-light);
  }
  .icon-disc { fill: var(--brand-red); stroke: var(--card-dark); stroke-width: 3; }
  .icon-glyph { fill: var(--card-dark); }
  .icon-cut { fill: var(--brand-red); }
  .icon-line { fill: none; stroke: var(--card-dark); stroke-width: 2; }
</style>
</head>
<body>
<main class="canvas">

  <!-- Back of card: brand, tagline and website -->
  <svg class="card card-back" viewBox="0 0 700 400" aria-label="Business card back">
    <rect class="card-bg" width="700" height="400"/>
    <path class="card-red" d="M0 330 H230 C285 330 265 220 345 220 H700 V400 H0 Z"/>
    <rect class="card-red" x="170" y="60" width="360" height="120"/>
    <text class="brand-name" x="350" y="117" text-anchor="middle" font-size="31">NORVANE BUILDERS</text>
    <text class="brand-name" x="350" y="154" text-anchor="middle" font-size="21">LIMITED</text>
    <text class="tagline" x="350" y="202" text-anchor="middle">QUALITY STARTS FROM THE GROUND UP</text>
    <text class="site-url" x="470" y="300" text-anchor="middle">www.norvanebuilders-example.com</text>
  </svg>

  <!-- Front of card: contact details -->
  <svg class="card card-front" viewBox="0 0 700 400" aria-label="Business card front">
    <rect class="card-bg" width="700" height="400"/>
    <path class="card-red" d="M0 0 H270 A250 250 0 0 1 270 400 H0 Z"/>

    <text class="brand-name" x="165" y="198" text-anchor="middle" font-size="27">NORVANE BUILDERS</text>
    <text class="brand-name" x="165" y="230" text-anchor="middle" font-size="19">LIMITED</text>

    <text class="person-name" x="380" y="62"><tspan class="person-first">DANA</tspan><tspan class="person-last"> KELLER</tspan></text>
    <text class="person-role" x="382" y="86">Solution Manager</text>

    <!-- person icon -->
    <g transform="translate(336 105)">
      <circle class="icon-disc" r="19"/>
      <circle class="icon-glyph" cy="-4" r="5"/>
      <path class="icon-glyph" d="M-9 9 C-9 1 9 1 9 9 Z"/>
    </g>

    <!-- phone -->
    <g transform="translate(361 160)">
      <circle class="icon-disc" r="19"/>
      <path class="icon-glyph" d="M-8 -7 L-4 -9 L-1 -3 L-4 -1 C-2 3 1 5 3 6 L5 3 L10 6 L8 10 C0 10 -9 1 -8 -7 Z"/>
    </g>
    <text class="contact-line" x="405" y="166">709-555-0147</text>

    <!-- fax / printer -->
    <g transform="translate(370 215)">
      <circle class="icon-disc" r="19"/>
      <rect class="icon-glyph" x="-5" y="-10" width="10" height="5"/>
      <rect class="icon-glyph" x="-10" y="-4" width="20" height="9" rx="1.5"/>
      <rect class="icon-cut" x="-6" y="1" width="12" height="2"/>
      <rect class="icon-glyph" x="-5" y="4" width="10" height="6"/>
    </g>
    <text class="contact-line" x="414" y="221">709-555-0192</text>

    <!-- web -->
    <g transform="translate(364 270)">
      <circle class="icon-disc" r="19"/>
      <circle class="icon-line" r="9"/>
      <ellipse class="icon-line" rx="4" ry="9"/>
      <line class="icon-line" x1="-9" y1="0" x2="9" y2="0"/>
    </g>
    <text class="contact-line" x="408" y="276">www.norvanebuilders-example.com</text>

    <!-- address pin -->
    <g transform="translate(342 330)">
      <circle class="icon-disc" r="19"/>
      <path class="icon-glyph" d="M0 11 C-4 5 -7 1 -7 -3 A7 7 0 0 1 7 -3 C7 1 4 5 0 11 Z"/>
      <circle class="icon-cut" cy="-3" r="2.5"/>
    </g>
    <text class="contact-line" x="386" y="326">42 Brenton Street</text>
    <text class="contact-line" x="386" y="347">Elk Harbour, NL B3K 7T2</text>
  </svg>

</main>
</body>
</html>
```